Task Scheduling Web App

I have a basic web app that I need designed. It must be mobile-first but it needs to be responsive for desktop users as well.
1. Before beginning the exercise, the user inputs basic info on their country and age.
2. The user is then presented with two piles of cards (TASK or DAY), with the top card face up. They have 20 seconds before their combination is set, during which they can replace either of the cards at random as many times as they like. At any time they find a combination they’re happy with, they can progress to the next screen. If the clock runs out the combination is set based on whatever cards are showing at the time and they’re moved on to the next screen.
3. The user is presented with a blank graph; x axis is ‘How important is it?’, y axis is ‘How often does it need to be done?’. The two cards they picked in the previous screen are combined to create a COMBO and the user must place a mark somewhere on the graph to represent how important they believe the scheduled task to be vs how often it will need to be done.
4. Once the user has picked a spot on the graph, options appear for them to re-do the exercise by choosing a new combo or to progress and see how their peers are organising their tasks.
5. If they choose to view insights, they must login with Quelvorn so a popup will appear to facilitate this.
6. After logging in with Quelvorn, users can view the top 10 combinations for their demographic listed and mapped on a graph. This information is based on the selection and ranking of combinations by other users.

```html
<!DOCTYPE html>
<html lang="en">
<head>
<meta charset="utf-8">
<title>Task Scheduling App – Screens</title>
<link href="https://fonts.googleapis.com/css2?family=Comfortaa:wght@400;600;700&family=Open+Sans:wght@400;600;700&display=swap" rel="stylesheet">
<style>
  :root{
    --stage:#766e78;
    --navy:#2b2a5c;
    --blue:#169ad8;
    --blue-dark:#0d86c4;
    --sky:#d3e7f8;
    --sky-soft:#eef6fd;
    --white:#ffffff;
    --overlay:#5d6a78;
    --brand:#1a4f8f;
  }
  *{box-sizing:border-box;margin:0;padding:0}
  html,body{width:1200px;height:960px;overflow:hidden}
  body{background:var(--stage);font-family:'Comfortaa',sans-serif;color:var(--navy)}
  .board{position:relative;width:1200px;height:960px;display:grid;
    grid-template-columns:repeat(3,260px);grid-template-rows:repeat(2,450px);
    gap:30px 60px;padding:20px 150px}
  .screen{position:relative;overflow:hidden;box-shadow:0 10px 24px rgba(0,0,0,.35)}
  .backdrop{position:absolute;inset:0;
    background:linear-gradient(160deg,var(--sky) 0%,var(--sky-soft) 45%,var(--white) 100%)}
  .screen.login .backdrop{background:linear-gradient(160deg,#66717e 0%,var(--overlay) 60%,#556272 100%)}
  .title{position:absolute;left:0;right:0;text-align:center;font-weight:400;font-size:25px}
  .timer{position:absolute;left:0;right:0;top:64px;text-align:center;font-size:22px;font-weight:700;letter-spacing:1px}

  /* Pick a combo */
  .card{position:absolute;left:30px;width:200px;height:110px;background:var(--white);
    box-shadow:2px 4px 8px rgba(40,40,90,.25);display:flex;align-items:center;justify-content:center;font-size:20px}
  .card .shuffle{position:absolute;right:10px;bottom:10px;width:18px;height:18px}
  .divider{position:absolute;left:24px;right:24px;top:232px;height:2px;background:var(--navy)}
  .next{position:absolute;right:20px;bottom:30px;width:38px;height:38px}

  /* User info */
  .status{position:absolute;top:0;left:0;right:0;height:18px;display:flex;justify-content:space-between;
    align-items:center;padding:0 10px;font-family:'Open Sans',sans-serif;font-size:8px;color:#222}
  .pill{position:absolute;left:40px;width:180px;height:34px;border-radius:17px;background:var(--blue);
    color:var(--white);font-family:'Open Sans',sans-serif;font-weight:700;font-size:10px;letter-spacing:.5px;
    display:flex;align-items:center;padding-left:24px;box-shadow:0 3px 5px rgba(0,60,120,.3)}
  .pill .chev{position:absolute;right:6px;top:6px;width:22px;height:22px;border-left:1px solid rgba(255,255,255,.5)}
  .go{position:absolute;left:40px;top:270px;width:180px;height:38px;border:2px solid var(--navy);border-radius:10px;
    display:flex;align-items:center;justify-content:center;font-size:20px;box-shadow:0 3px 5px rgba(40,40,90,.25)}

  /* Graph */
  .graph{position:absolute;left:0;top:0;width:260px}
  .combo{position:absolute;left:24px;width:212px}
  .combo .picks{display:flex;height:52px}
  .combo .picks span{flex:1;background:var(--blue);color:var(--white);display:flex;align-items:center;justify-content:center;font-size:16px}
  .combo .picks span+span{border-left:1px solid var(--blue-dark)}
  .combo .result{height:40px;border:1px solid var(--navy);border-top:none;background:rgba(255,255,255,.6);
    display:flex;align-items:center;justify-content:center;font-size:17px}
  .action{position:absolute;bottom:0;height:50px;background:var(--navy);color:var(--white);
    display:flex;align-items:center;gap:8px;padding:0 10px;font-size:12px;line-height:1.1}
  .action svg{width:22px;height:22px;flex:none}

  /* Login */
  .popup{position:absolute;left:26px;top:70px;width:208px;padding-bottom:22px;background:var(--white);box-shadow:0 6px 14px rgba(0,0,0,.4)}
  .popup .close{position:absolute;right:-8px;top:-22px;width:14px;height:14px}
  .popup header{height:80px;background:var(--brand);color:var(--white);display:flex;align-items:center;justify-content:center;
    font-family:'Open Sans',sans-serif;font-weight:700;font-size:20px}
  .insights{margin:18px auto 0;width:130px;height:26px;border:1.5px solid var(--brand);color:var(--brand);
    font-family:'Open Sans',sans-serif;font-size:10px;display:flex;align-items:center;justify-content:center}
  .field{margin:16px 18px 0;height:26px;border-bottom:1px solid #c9d3df;display:flex;align-items:flex-end;gap:6px;padding-bottom:4px;
    font-family:'Open Sans',sans-serif;font-size:9px;color:#8aa2c0}
  .field svg{width:12px;height:12px}
  .login-btn{margin:20px 18px 0;height:28px;background:var(--brand);color:var(--white);font-family:'Open Sans',sans-serif;
    font-size:11px;display:flex;align-items:center;justify-content:center}

  /* Top ten */
  .lead{position:absolute;left:16px;right:16px;top:18px;text-align:center;font-size:15px;line-height:1.25}
  .top-list{position:absolute;left:16px;right:16px;top:68px;display:grid;grid-template-columns:1fr 1fr;grid-auto-flow:column;
    grid-template-rows:repeat(5,24px);column-gap:10px;list-style:none;font-size:11px}
  .top-list li{display:flex;justify-content:space-between;align-items:center;border-bottom:1px solid rgba(43,42,92,.12)}
  .top-list li::after{content:"›";font-size:13px}
</style>
</head>
<body>
<main class="board">

  <!-- Pick a combo -->
  <section class="screen pick">
    <div class="backdrop" role="img" aria-label="Soft blue backdrop with flowing wave lines"></div>
    <h1 class="title" style="top:30px">Pick a Combo</h1>
    <div class="timer">00:20</div>
    <div class="card" style="top:108px">Task
      <svg class="shuffle" viewBox="0 0 20 20" fill="none" stroke="var(--navy)" stroke-width="2"><circle cx="10" cy="10" r="8"/><path d="M13 7a4 4 0 1 0 0 6"/></svg></div>
    <div class="divider"></div>
    <div class="card" style="top:250px">Day
      <svg class="shuffle" viewBox="0 0 20 20" fill="none" stroke="var(--navy)" stroke-width="2"><circle cx="10" cy="10" r="8"/><path d="M13 7a4 4 0 1 0 0 6"/></svg></div>
    <svg class="next" viewBox="0 0 40 40" fill="none" stroke="var(--navy)" stroke-width="2"><circle cx="20" cy="20" r="17"/><path d="M12 21 L28 12 L21 28 L19 22 Z" fill="var(--navy)"/></svg>
  </section>

  <!-- User info -->
  <section class="screen info">
    <div class="backdrop" role="img" aria-label="Soft blue backdrop with flowing wave lines"></div>
    <div class="status"><span>●●●○○ VELTRA</span><span>4:21 PM</span><span>22%</span></div>
    <h1 class="title" style="top:80px;font-size:28px">User Info</h1>
    <div class="pill" style="top:160px">COUNTRY
      <svg class="chev" viewBox="0 0 22 22" fill="none" stroke="var(--white)" stroke-width="1.5"><circle cx="13" cy="11" r="8"/><path d="M9 9 L13 14 L17 9"/></svg></div>
    <div class="pill" style="top:206px">AGE RANGE
      <svg class="chev" viewBox="0 0 22 22" fill="none" stroke="var(--white)" stroke-width="1.5"><circle cx="13" cy="11" r="8"/><path d="M9 9 L13 14 L17 9"/></svg></div>
    <div class="go">GO!</div>
  </section>

  <!-- Prioritize combo (empty) -->
  <section class="screen prioritize">
    <div class="backdrop" role="img" aria-label="Soft blue backdrop with flowing wave lines"></div>
    <h1 class="title" style="top:30px;font-size:24px">Prioritize Combo</h1>
    <svg class="graph" viewBox="0 0 260 450" font-family="Open Sans, sans-serif" fill="var(--navy)">
      <path d="M40 100 V270 H232 V260" fill="none" stroke="var(--navy)" stroke-width="1.5"/>
      <path d="M36 100 H40" stroke="var(--navy)"/>
      <text x="12" y="104" font-size="8">Huge</text>
      <text x="14" y="282" font-size="8">None</text>
      <text x="40" y="282" font-size="8">1x</text>
      <text x="224" y="256" font-size="8">10x</text>
      <text transform="translate(30 185) rotate(-90)" font-size="8" text-anchor="middle">How important is it?</text>
      <text x="136" y="282" font-size="8" text-anchor="middle">How often does it need to be done?</text>
    </svg>
    <div class="combo" style="top:310px">
      <div class="picks"><span>Task</span><span>Day</span></div>
      <div class="result">Combo</div>
    </div>
  </section>

  <!-- Top ten -->
  <section class="screen top">
    <div class="backdrop" role="img" aria-label="Soft blue backdrop with flowing wave lines"></div>
    <p class="lead">These are the top 10 combos<br>chosen by your peers</p>
    <ol class="top-list">
      <li>1. Task/Day</li><li>2. Task/Day</li><li>3. Task/Day</li><li>4. Task/Day</li><li>5. Task/Day</li>
      <li>6. Task/Day</li><li>7. Task/Day</li><li>8. Task/Day</li><li>9. Task/Day</li><li>10. Task/Day</li>
    </ol>
    <svg class="graph" viewBox="0 0 260 450" font-family="Open Sans, sans-serif" fill="var(--navy)">
      <path d="M40 210 V380 H232 V370" fill="none" stroke="var(--navy)" stroke-width="1.5"/>
      <text x="12" y="214" font-size="8">Huge</text>
      <text x="14" y="392" font-size="8">None</text>
      <text x="40" y="392" font-size="8">1x</text>
      <text x="224" y="366" font-size="8">10x</text>
      <text transform="translate(30 295) rotate(-90)" font-size="8" text-anchor="middle">How important is it?</text>
      <text x="136" y="392" font-size="8" text-anchor="middle">How often does it need to be done?</text>
      <path d="M58 370 C60 310 70 280 90 262 S140 250 170 252 S210 262 218 225" fill="none" stroke="var(--navy)" stroke-width="1.2"/>
      <g font-size="6">
        <circle cx="59" cy="350" r="2"/><text x="63" y="352">1</text>
        <circle cx="62" cy="325" r="2"/><text x="66" y="327">2</text>
        <circle cx="68" cy="300" r="2"/><text x="72" y="302">3</text>
        <circle cx="76" cy="282" r="2"/><text x="80" y="284">4</text>
        <circle cx="90" cy="264" r="2"/><text x="93" y="261">5</text>
        <circle cx="110" cy="256" r="2"/><text x="113" y="253">6</text>
        <circle cx="135" cy="252" r="2"/><text x="138" y="249">7</text>
        <circle cx="165" cy="252" r="2"/><text x="168" y="249">8</text>
        <circle cx="205" cy="258" r="2"/><text x="208" y="262">9</text>
        <circle cx="218" cy="226" r="2"/><text x="210" y="222">10</text>
      </g>
    </svg>
    <div class="action" style="left:60px;right:0;justify-content:center;font-size:16px">New Combo</div>
  </section>

  <!-- Login popup -->
  <section class="screen login">
    <div class="backdrop" role="img" aria-label="Dimmed slate backdrop with flowing wave lines"></div>
    <div class="popup">
      <svg class="close" viewBox="0 0 14 14"><circle cx="7" cy="7" r="7" fill="#222"/><path d="M4.5 4.5 L9.5 9.5 M9.5 4.5 L4.5 9.5" stroke="#fff" stroke-width="1.4"/></svg>
      <header>Quelvorn</header>
      <div class="insights">Get Insights</div>
      <div class="field" style="margin-top:22px"></div>
      <div class="field"><svg viewBox="0 0 12 12"><rect x="1" y="2.5" width="10" height="7" fill="#1a4f8f"/><path d="M1 2.5 L6 7 L11 2.5" stroke="#fff" fill="none"/></svg>Email</div>
      <div class="field"><svg viewBox="0 0 12 12"><rect x="2" y="5" width="8" height="6" fill="#1a4f8f"/><path d="M4 5 V3.5 a2 2 0 0 1 4 0 V5" stroke="#1a4f8f" fill="none" stroke-width="1.3"/></svg>Password</div>
      <div class="login-btn">Login</div>
    </div>
  </section>

  <!-- Prioritize combo with options -->
  <section class="screen prioritize">
    <div class="backdrop" role="img" aria-label="Soft blue backdrop with flowing wave lines"></div>
    <h1 class="title" style="top:30px;font-size:24px">Prioritize Combo</h1>
    <svg class="graph" viewBox="0 0 260 450" font-family="Open Sans, sans-serif" fill="var(--navy)">
      <path d="M40 90 V250 H232 V240" fill="none" stroke="var(--navy)" stroke-width="1.5"/>
      <path d="M36 90 H40" stroke="var(--navy)"/>
      <text x="12" y="94" font-size="8">Huge</text>
      <text x="14" y="262" font-size="8">None</text>
      <text x="40" y="262" font-size="8">1x</text>
      <text x="224" y="236" font-size="8">10x</text>
      <text transform="translate(30 170) rotate(-90)" font-size="8" text-anchor="middle">How important is it?</text>
      <text x="136" y="262" font-size="8" text-anchor="middle">How often does it need to be done?</text>
    </svg>
    <div class="combo" style="top:280px">
      <div class="picks"><span>Task</span><span>Day</span></div>
      <div class="result">Combo</div>
    </div>
    <div class="action" style="left:0;width:122px">
      <svg viewBox="0 0 22 22"><circle cx="11" cy="11" r="10" fill="#fff"/><path d="M11 6 V16 M6 11 H16" stroke="var(--navy)" stroke-width="2.5"/></svg>New<br>Combo</div>
    <div class="action" style="right:0;width:130px">
      <svg viewBox="0 0 22 22"><circle cx="11" cy="11" r="10" fill="#fff"/><circle cx="7.5" cy="12" r="3" fill="var(--navy)"/><circle cx="14.5" cy="12" r="3" fill="var(--navy)"/></svg>See What<br>Others Are Doing</div>
  </section>

</main>
</body>
</html>
```